Vodka label, brand name: LATE BIRCH

We are looking for a vodka label design, which will print on paper or plastic (not a bottle printing)

We are small distilling company: Ferncliff Distillery. Located in Toronto, Canada. Our business is small batches of handcrafted very smooth vodka production. 40% abv. Made from cane sugar and spring water.

Our audience pretty mach everyone who consume vodka/alcohol, we are not targeting any specific group.

Back label should have barcode, government warning and this text:

Our vodka is handmade in small batches to the highest standards befitting the true vodka perfectionist. We use silk filtering process for exceptional purity, clarity, and smoothness. It is distilled 6 times from the finest organic cane sugar using only the best Canadian spring water. Discover the smooth, clear taste for yourself.
Distilled and Bottled by
Ferncliff Distillery Inc.
Toronto, Canada

Government Warning: In accordance to the Surgeon General, women should not drink alcoholic beverages during pregnancy because of the risk of birth defects. Consumption of alcoholic beverages impairs your ability to drive a car or operate machinery and may cause health problems.

Size of the bottle as follows (see example in the attachment) :
Volume: 750ml
Total height: 330mm
Body diameter: 77mm
Closure: Bar Top
Silver synthetic cork

Target Market(s)

Colors

Designer to choose colors to be used in the design.

Requirements
Must have
• Incorporate the name: LATE BIRCH
• Incorporate: DISTILLED FROM ORGANIC CANE SUGAR
• Back bottle label should have barcode, government warning and this text:
• Our vodka is handmade in small batches to the highest standards befitting the true vodka perfectionist. We use silk filtering process for exceptional purity, clarity, and smoothness. It is distilled 6 times from the finest organic cane sugar using only the best Canadian spring water. Discover the smooth, clear taste for yourself.
• Distilled and Bottleb by
• Ferncliff Distillery Inc.
• Toronto, Canada
• Government Warning: In accordance to the Surgeon General, women should not drink alcoholic beverages during pregnancy because of the risk of birth defects. Consumption of alcoholic beverages impairs your ability to drive a car or operate machinery and may cause health problems.
Nice to have
• 1) To show in wording or design it was Handmade
• 2) To show in wording or design it was made with Natural Spring Water
• To show in wording or design it was made in small batches
• 3) To show in wording or design it was made local in Toronto, Canada
• "The Six" "The 6ix"- is the nick name of city of Toronto that's just for designer to consider and not mandatory to implement on design
Should not have
• We try to lower cost of printing , so design should be for digital printing without Gold, Silver or any other color which requires foil application on label and will increase cost of printing.
• No copy paste from internet images. Such designs will be ignored and reported to website admin. Authentic design work only.
• Please try not to use clock or any related to that images. Its nothing to do with clock, its too naive to show 6 pm on the watches in your design. Its could be time of the day (evening), after work, the six as nick name of Toronto. But not clock or watches .

```html
<!DOCTYPE html>
<html lang="en">
<head>
<meta charset="utf-8">
<title>Late Birch Vodka Label</title>
<link rel="stylesheet" href="https://fonts.googleapis.com/css2?family=Arimo:wght@400&family=Oswald:wght@600&display=swap">
<style>
  :root {
    --brand-red: #e80000;
    --label-grey: #d6d6d6;
    --label-white: #ffffff;
    --backdrop: #b8b8b8;
    --lettering-tint: #f3c9c9;
  }
  * { margin: 0; padding: 0; box-sizing: border-box; }
  html, body { width: 1200px; height: 800px; overflow: hidden; }
  body {
    background: var(--backdrop);
    font-family: "Arimo", Arial, sans-serif;
    color: var(--brand-red);
    position: relative;
  }
  .front-label, .neck-band {
    position: absolute;
    left: 290px;
    width: 620px;
    background: linear-gradient(90deg, var(--label-grey) 0%, var(--label-white) 100%);
  }
  .front-label { top: 30px; height: 595px; }
  .neck-band { top: 653px; height: 117px; }

  .hand-lettering {
    position: absolute;
    left: 30px; top: 75px;
    width: 253px; height: 283px;
    background: linear-gradient(160deg, var(--lettering-tint), rgba(243, 201, 201, 0.35));
  }

  .brand-band {
    position: absolute;
    left: 333px; top: 0;
    width: 149px; height: 498px;
    background: var(--brand-red);
  }
  .brand-ring {
    position: absolute;
    left: 39px; top: 18px;
    width: 86px; height: 86px;
    border: 3px solid var(--label-white);
    border-radius: 50%;
  }
  .brand-name {
    position: absolute;
    left: 82px; top: 290px;
    transform: translate(-50%, -50%) rotate(-90deg);
    white-space: nowrap;
    font-size: 54px;
    line-height: 1;
    letter-spacing: 1px;
    color: var(--label-white);
  }

  .government-warning {
    position: absolute;
    right: 305px; top: 395px;
    width: 240px;
    text-align: right;
    font-size: 10.2px;
    line-height: 13.6px;
  }

  .story-text {
    position: absolute;
    left: 500px; top: 22px;
    height: 468px;
    writing-mode: vertical-rl;
    transform: rotate(180deg);
    font-size: 9.8px;
    line-height: 21.5px;
    white-space: nowrap;
  }

  .producer {
    position: absolute;
    left: 39px; top: 517px;
    font-size: 15px;
    line-height: 20px;
  }
  .origin-claim {
    position: absolute;
    left: 355px; top: 525px;
    transform: translateX(-50%);
    text-align: center;
    font-family: "Oswald", "Arial Narrow", sans-serif;
    font-weight: 600;
    font-size: 15.5px;
    line-height: 22px;
    letter-spacing: 0.3px;
    white-space: nowrap;
  }
  .strength, .volume {
    position: absolute;
    right: 39px;
    font-size: 15.5px;
    line-height: 1;
  }
  .strength { top: 524px; }
  .volume { top: 554px; }

  .leaf-emblem {
    position: absolute;
    left: 275px; top: 22px;
    width: 71px; height: 73px;
    background: var(--brand-red);
    border-radius: 40% 40% 20% 20%;
  }
</style>
</head>
<body>
  <section class="front-label">
    <div class="hand-lettering" role="img" aria-label="Red hand lettering reading Hand made vodka"></div>

    <div class="brand-band">
      <div class="brand-ring"></div>
      <div class="brand-name">LATE BIRCH</div>
    </div>

    <p class="government-warning">Government Warning:<br>In accordance to the Surgeon General,<br>women should not drink alcoholic beverages<br>during pregnancy because of the risk of birth<br>defects. Consumption of alcoholic beverages<br>impairs your ability to drive a car or operate<br>machinery and may cause health problems.</p>

    <p class="story-text">Our vodka is handmade in small batches to the highest standards<br>befitting the true vodka perfectionist. We use silk filtering process for exceptional purity,<br>clarity, and smoothness. It is distilled 6 times from the finest organic cane sugar using only the<br>best Canadian spring water. Discover the smooth, clear taste for yourself.</p>

    <p class="producer">Distilled and Bottled by<br>Ferncliff Distillery<br>Inc.Toronto, Canada</p>

    <p class="origin-claim">DISTILLED FROM ORGANIC<br>CANE SUGAR</p>

    <p class="strength">40% abv</p>
    <p class="volume">750ml</p>
  </section>

  <section class="neck-band">
    <div class="leaf-emblem" role="img" aria-label="Red maple leaf emblem"></div>
  </section>
</body>
</html>
```